Town Planning Consultants require lstationary design

Require a design to be used for our letterhead and report cover page. We have an approved logo.
we have attached our logo, and our temporary letterhead/cover page (SEE Cover) which we currently adapt for both purposes in the interim pending a permanent design. I have also attached an example (example report cover) of a report cover page that I like. perhaps similar with our colour scheme

Target Market(s)

?

Industry/Entity Type

Town

Colors
249fd4
3176b5

Requirements
Must have
• colours to match logo
• the text content in existing letterhead

```html
<!DOCTYPE html>
<html lang="en">
<head>
<meta charset="utf-8">
<title>Statement of Environmental Effects – Report Cover</title>
<link href="https://fonts.googleapis.com/css2?family=Roboto+Condensed:wght@300;400&family=Open+Sans:ital,wght@0,400;0,600;0,700;1,700&family=Roboto:wght@300;400&display=swap" rel="stylesheet">
<style>
  :root {
    --brand-blue: #2fa8d9;
    --sheet-grey: #efeff0;
    --band-grey: #a3a3a3;
    --ink: #1a1a1a;
    --muted: #808080;
    --white: #ffffff;
    --photo-light: #a9bcc0;
    --photo-dark: #7b948c;
  }
  * { margin: 0; padding: 0; box-sizing: border-box; }
  html, body { width: 900px; height: 1200px; overflow: hidden; background: var(--white); }
  .cover {
    position: relative;
    width: 900px;
    height: 1200px;
    background: var(--white);
    font-family: "Open Sans", Arial, sans-serif;
    overflow: hidden;
  }
  .cover__shapes { position: absolute; inset: 0; }
  .brand {
    position: absolute;
    left: 44px;
    top: 150px;
    display: flex;
    align-items: center;
    gap: 16px;
    color: var(--white);
    font-family: "Open Sans", Arial, sans-serif;
    font-weight: 400;
    font-size: 76px;
    line-height: 1;
    letter-spacing: -1px;
  }
  .brand__mark { width: 34px; height: 34px; background: var(--white); }
  .contact {
    position: absolute;
    right: 42px;
    top: 138px;
    text-align: right;
    color: var(--muted);
    font-size: 11px;
    line-height: 15.5px;
  }
  .contact__company { font-weight: 700; font-size: 14px; margin-bottom: 6px; }
  .contact__address { margin-bottom: 6px; }
  .contact__line { display: flex; justify-content: flex-end; align-items: center; gap: 6px; }
  .contact__line svg { width: 10px; height: 10px; fill: var(--brand-blue); }
  .report-type {
    position: absolute;
    left: 42px;
    top: 520px;
    font-weight: 700;
    font-style: italic;
    font-size: 17px;
    color: var(--ink);
  }
  .report-title {
    position: absolute;
    left: 40px;
    top: 560px;
    font-family: "Roboto Condensed", Arial, sans-serif;
    font-weight: 300;
    font-size: 70px;
    line-height: 60px;
    color: var(--brand-blue);
  }
  .site-photo {
    position: absolute;
    left: 42px;
    top: 706px;
    width: 408px;
    height: 254px;
    background: linear-gradient(180deg, var(--photo-light) 0%, var(--photo-dark) 100%);
  }
  .site-address {
    position: absolute;
    left: 42px;
    top: 962px;
    font-family: "Roboto", Arial, sans-serif;
    font-weight: 300;
    font-size: 35px;
    letter-spacing: -0.3px;
    color: var(--ink);
  }
  .credits {
    position: absolute;
    left: 42px;
    top: 1097px;
    font-family: "Roboto Condensed", Arial, sans-serif;
    font-size: 12.5px;
    line-height: 17px;
    color: var(--muted);
  }
  .credits b { font-family: "Open Sans", Arial, sans-serif; font-weight: 700; letter-spacing: 0.3px; }
  .services {
    position: absolute;
    right: 42px;
    top: 1162px;
    display: flex;
    gap: 12px;
    align-items: center;
    color: var(--white);
    font-weight: 700;
    font-size: 14px;
    letter-spacing: 0.2px;
  }
  .services__dot { width: 4px; height: 4px; background: var(--white); }
</style>
</head>
<body>
<div class="cover">
  <svg class="cover__shapes" width="900" height="1200" viewBox="0 0 900 1200">
    <polygon points="900,0 515,203 900,355" fill="var(--sheet-grey)"/>
    <polygon points="0,0 900,0 0,469" fill="var(--brand-blue)"/>
    <polygon points="0,1180 295,1180 275,1200 0,1200" fill="var(--band-grey)"/>
    <polygon points="344,1144 900,1144 900,1200 285,1200" fill="var(--brand-blue)"/>
  </svg>

  <div class="brand"><span class="brand__mark"></span>Norvale</div>

  <div class="contact">
    <div class="contact__company">Norvale Planning Pty Ltd</div>
    <div class="contact__address">18 Harbour Ridge Road,<br>Coralbay, NSW 2490</div>
    <div class="contact__line">+61 (2) 5550 1234
      <svg viewBox="0 0 10 10"><path d="M2 0.5 L3.6 2.6 L2.8 3.6 Q4 6 6.4 7.2 L7.4 6.4 L9.5 8 L8.6 9.5 Q3.5 9 0.5 1.4 Z"/></svg></div>
    <div class="contact__line">+61 (0)400 555 210
      <svg viewBox="0 0 10 10"><path d="M2.5 0 H7.5 V10 H2.5 Z M3.5 1 V8 H6.5 V1 Z"/></svg></div>
    <div class="contact__line">info@norvale.com.au
      <svg viewBox="0 0 10 10"><path d="M0 1.5 H10 V8.5 H0 Z M1 2.5 L5 5.5 L9 2.5 Z" fill-rule="evenodd"/></svg></div>
  </div>

  <div class="report-type">Proposed Additions to Existing Dwelling</div>
  <h1 class="report-title">Statement of<br>Environmental Effects</h1>

  <div class="site-photo" role="img" aria-label="Photograph of the site: waterfront homes above a river"></div>

  <div class="site-address">12 Wattle Crescent, RIVERSIDE</div>

  <div class="credits">
    Prepared for: <b>M. Harlow</b><br>
    Prepared by: <b>K. Dalton</b><br>
    Reviewed by: <b>R. Mancini</b><br>
    Dated: <b>June, 2016</b>
  </div>

  <div class="services">
    <span>PLANNING</span><span class="services__dot"></span>
    <span>DEVELOPMENT</span><span class="services__dot"></span>
    <span>URBAN DESIGN</span><span class="services__dot"></span>
    <span>CONSULTANTS</span>
  </div>
</div>
</body>
</html>
```